Brightwell Comfort Contractors - Ductless Mini-Split Ad Creative Brief 4 qp ad images

Our Offers (Must Be Clearly Visible in the Design)
100% Satisfaction Guarantee
"We guarantee to keep you cool, or your money back! If you're not happy after we’ve had a chance to fix it, we’ll refund you!"

5-Year Labor Warranty
"That’s right – a 5-year labor warranty! No maintenance agreement required, just clean your filters each month!"

Chill-Wave Season 2025
"LIMITED-TIME OFFER: Get $999 off any ductless mini-split installation!"

Transparent Pricing
"What you see is what you pay—NO hidden fees!"

Ad Design Guidelines
Primary Focus: Ductless Mini-Split A/C Systems ONLY
Color Scheme: Must incorporate Brightwell Comfort Contractors' main colors with a hint of yellow to catch attention.
Look at truck wrap to get a feel for the border of ad image creative
Branding Elements: Include Brightwell Comfort logo prominently.
Contact Details: Display phone number clearly.
Trust Builders: Feature Chatterly & Zorvex review elements to enhance credibility.
Visibility: The offers must be clear and readable but not overcrowded. Prioritize readability and clean design.
Final Notes
Ensure the design is high-converting and visually engaging while maintaining a professional, premium feel.
The ad creatives will be used for ductless mini-split A/C systems only—this must be clear in the design messaging.
Feel Free to use your expertise and experience to make this better
Thank you 555-317-2946

```html
<!DOCTYPE html>
<html lang="en">
<head>
<meta charset="utf-8">
<title>Brightwell Comfort Contractors – Ductless Mini-Split Ads</title>
<link rel="stylesheet" href="https://fonts.googleapis.com/css2?family=Poppins:wght@600;700;800&family=Figtree:wght@400&display=swap">
<style>
  :root{
    --backdrop:#595d60;
    --red:#c4262e;
    --blue:#0a6fbf;
    --white:#ffffff;
    --head-font:"Poppins", sans-serif;
    --body-font:"Figtree", sans-serif;
  }
  *{margin:0;padding:0;box-sizing:border-box}
  html,body{width:1200px;height:1200px;overflow:hidden}
  body{background:var(--backdrop);position:relative;font-family:var(--body-font)}

  .ad-card{position:absolute;width:507px;height:507px;overflow:hidden;background:var(--white);
    box-shadow:0 2px 6px rgba(0,0,0,.35)}
  .ad-card--warranty{left:84px;top:82px;--ring:var(--red);--band:var(--red);--stripe:var(--blue)}
  .ad-card--guarantee{left:611px;top:82px;--ring:var(--blue);--band:var(--blue);--stripe:var(--red)}
  .ad-card--season{left:84px;top:613px;--ring:var(--blue);--band:var(--blue);--stripe:var(--red)}
  .ad-card--pricing{left:611px;top:613px;--ring:var(--red);--band:var(--red);--stripe:var(--blue)}

  .ad-art{position:absolute;inset:0;width:507px;height:507px}
  .ad-art .ring{fill:var(--ring)}
  .ad-art .gap{fill:var(--white)}
  .ad-art .stripe{fill:var(--stripe)}
  .ad-art .band{fill:var(--band)}

  .brand{position:absolute;left:21px;top:34px;width:160px;text-align:center}
  .brand-mark{width:48px;height:48px;border-radius:50%;background:var(--red);margin:0 auto 12px}
  .brand-name{font-family:var(--head-font);font-weight:700;color:var(--blue);
    font-size:14px;line-height:16px;text-transform:uppercase;letter-spacing:.5px}

  .headline{position:absolute;font-family:var(--head-font);font-weight:700;line-height:1;white-space:nowrap}
  .headline .accent{color:var(--red);display:block}
  .headline .lead{color:var(--blue);display:block}

  .ad-card--warranty .headline{left:38px;top:180px}
  .ad-card--warranty .accent{font-size:132px;font-weight:800;line-height:100px;letter-spacing:-2px}
  .ad-card--warranty .lead{font-size:33px;line-height:30px;margin-top:6px}

  .ad-card--guarantee .headline{left:31px;top:232px}
  .ad-card--guarantee .accent{font-size:68px;font-weight:800;line-height:66px;letter-spacing:-2px}
  .ad-card--guarantee .percent{font-size:36px;vertical-align:22px;letter-spacing:0}
  .ad-card--guarantee .lead{font-size:28px;line-height:33px}

  .ad-card--season .headline{left:42px;top:221px}
  .ad-card--season .accent{font-size:40px;line-height:36px}
  .ad-card--season .lead{font-size:32px;line-height:33px;margin-top:1px}

  .ad-card--pricing .headline{left:41px;top:290px}
  .ad-card--pricing .lead{font-size:24px;line-height:30px}
  .ad-card--pricing .accent{font-size:44px;line-height:46px}

  .offer-copy{position:absolute;color:var(--white);font-family:var(--body-font);font-weight:400;white-space:nowrap}
  .ad-card--warranty .offer-copy{left:42px;top:441px;font-size:13px;line-height:14px}
  .ad-card--guarantee .offer-copy{left:31px;top:436px;font-size:13px;line-height:14px}
  .ad-card--season .offer-copy{left:45px;top:431px;font-size:16px;line-height:17.5px}
  .ad-card--pricing .offer-copy{left:46px;top:431px;font-size:17px;line-height:22px}
</style>
</head>
<body>

<!-- Warranty -->
<section class="ad-card ad-card--warranty">
  <svg class="ad-art" viewBox="0 0 817 817">
    <defs>
      <linearGradient id="photo-snow" x1="0" y1="0" x2="0" y2="1">
        <stop offset="0" stop-color="#c9c6c1"/><stop offset=".6" stop-color="#a8a49e"/><stop offset="1" stop-color="#eef0f2"/>
      </linearGradient>
    </defs>
    <circle class="ring" cx="770" cy="280" r="478"/>
    <g role="img" aria-label="Three technicians standing beside snow-covered ductless mini-split outdoor units">
      <circle cx="790" cy="320" r="488" fill="url(#photo-snow)"/>
    </g>
    <path class="gap" d="M0,680 C200,590 380,630 540,668 S760,705 817,688 L817,817 L0,817Z"/>
    <path class="stripe" d="M0,698 C200,610 380,645 540,688 S760,728 817,708 L817,817 L0,817Z"/>
    <path class="band" d="M0,712 C200,628 380,660 540,706 S760,748 817,728 L817,817 L0,817Z"/>
  </svg>
  <div class="brand"><div class="brand-mark"></div><p class="brand-name">Brightwell Comfort<br>Contractors</p></div>
  <h2 class="headline"><span class="accent">5</span><span class="lead">Year<br>Labor<br>Warranty</span></h2>
  <p class="offer-copy">That’s right – a 5-year labor warranty!<br>No maintenance agreement required,<br>just clean your filters each month!</p>
</section>

<!-- Guarantee -->
<section class="ad-card ad-card--guarantee">
  <svg class="ad-art" viewBox="0 0 817 817">
    <defs>
      <linearGradient id="photo-siding" x1="0" y1="0" x2="1" y2="1">
        <stop offset="0" stop-color="#cfc8bc"/><stop offset=".5" stop-color="#6a7f99"/><stop offset="1" stop-color="#3f4f66"/>
      </linearGradient>
    </defs>
    <circle class="ring" cx="770" cy="280" r="478"/>
    <g role="img" aria-label="Happy homeowner standing with a technician next to an outdoor air conditioning unit">
      <circle cx="790" cy="320" r="488" fill="url(#photo-siding)"/>
    </g>
    <path class="gap" d="M0,680 C200,590 380,630 540,668 S760,705 817,688 L817,817 L0,817Z"/>
    <path class="stripe" d="M0,698 C200,610 380,645 540,688 S760,728 817,708 L817,817 L0,817Z"/>
    <path class="band" d="M0,712 C200,628 380,660 540,706 S760,748 817,728 L817,817 L0,817Z"/>
  </svg>
  <div class="brand"><div class="brand-mark"></div><p class="brand-name">Brightwell Comfort<br>Contractors</p></div>
  <h2 class="headline"><span class="accent">100<span class="percent">%</span></span><span class="lead">Satisfaction<br>Guarantee</span></h2>
  <p class="offer-copy">We guarantee to keep you cool, or<br>your money back! If you're not<br>happy after we’ve had a chance to<br>fix it, we’ll refund you!</p>
</section>

<!-- Season offer -->
<section class="ad-card ad-card--season">
  <svg class="ad-art" viewBox="0 0 817 817">
    <defs>
      <linearGradient id="photo-yard" x1="0" y1="0" x2="1" y2="1">
        <stop offset="0" stop-color="#e6e3dc"/><stop offset=".5" stop-color="#b58f78"/><stop offset="1" stop-color="#2f5a95"/>
      </linearGradient>
    </defs>
    <circle class="ring" cx="770" cy="280" r="478"/>
    <g role="img" aria-label="Technician outdoors beside a home with a mini-split condenser">
      <circle cx="790" cy="320" r="488" fill="url(#photo-yard)"/>
    </g>
    <path class="gap" d="M0,680 C200,590 380,630 540,668 S760,705 817,688 L817,817 L0,817Z"/>
    <path class="stripe" d="M0,698 C200,610 380,645 540,688 S760,728 817,708 L817,817 L0,817Z"/>
    <path class="band" d="M0,712 C200,628 380,660 540,706 S760,748 817,728 L817,817 L0,817Z"/>
  </svg>
  <div class="brand"><div class="brand-mark"></div><p class="brand-name">Brightwell Comfort<br>Contractors</p></div>
  <h2 class="headline"><span class="accent">Chill-<br>Wave</span><span class="lead">Season<br>2025</span></h2>
  <p class="offer-copy">LIMITED-TIME OFFER:<br>Get $999 off any ductless<br>mini-split installation!</p>
</section>

<!-- Pricing -->
<section class="ad-card ad-card--pricing">
  <svg class="ad-art" viewBox="0 0 817 817">
    <defs>
      <linearGradient id="photo-stone" x1="0" y1="0" x2="1" y2="1">
        <stop offset="0" stop-color="#a67b52"/><stop offset=".5" stop-color="#c7c3bb"/><stop offset="1" stop-color="#3c4656"/>
      </linearGradient>
    </defs>
    <circle class="ring" cx="770" cy="280" r="478"/>
    <g role="img" aria-label="Technician servicing an opened mini-split outdoor unit against a stone wall">
      <circle cx="790" cy="320" r="488" fill="url(#photo-stone)"/>
    </g>
    <path class="gap" d="M0,680 C200,590 380,630 540,668 S760,705 817,688 L817,817 L0,817Z"/>
    <path class="stripe" d="M0,698 C200,610 380,645 540,688 S760,728 817,708 L817,817 L0,817Z"/>
    <path class="band" d="M0,712 C200,628 380,660 540,706 S760,748 817,728 L817,817 L0,817Z"/>
  </svg>
  <div class="brand"><div class="brand-mark"></div><p class="brand-name">Brightwell Comfort<br>Contractors</p></div>
  <h2 class="headline"><span class="lead">Transparent</span><span class="accent">Pricing</span></h2>
  <p class="offer-copy">What you see is what you<br>pay—NO hidden fees!</p>
</section>

</body>
</html>
```